Marlow & The Lanterns Album Cover -- 2

Hello,

I am looking for an album cover to help promote a hip hop song.

Artist Title: Granular Boomkeeperz
Song Title Marlow and The Lanterns

If you can add in my logo (Headphones on the lower right corner, that would be great.

```html
<!DOCTYPE html>
<html lang="en">
<head>
<meta charset="utf-8">
<title>Marlow and The Lanterns — Album Cover</title>
<link rel="stylesheet" href="https://fonts.googleapis.com/css2?family=Black+Ops+One&family=Cinzel:wght@400&display=swap">
<style>
  :root {
    --backdrop: #c9c6d7;
    --cover: #dddae9;
    --ink: #2b2842;
    --photo-light: #b4b1cb;
    --photo-dark: #565279;
    --accent: #d2456a;
  }
  html, body {
    margin: 0;
    padding: 0;
    width: 1200px;
    height: 793px;
    overflow: hidden;
    background: var(--backdrop);
  }
  .canvas {
    position: relative;
    width: 1200px;
    height: 793px;
  }
  .cover {
    position: absolute;
    left: 280px;
    top: 90px;
    width: 640px;
    height: 614px;
    background: var(--cover);
    overflow: hidden;
  }
  .cover-photo {
    position: absolute;
    left: 0;
    bottom: 0;
    width: 493px;
    height: 282px;
    background: linear-gradient(160deg, var(--photo-light) 0%, var(--photo-dark) 100%);
  }
  .title-frame {
    position: absolute;
    left: 86px;
    top: 74px;
    width: 471px;
    height: 200px;
    box-sizing: border-box;
    border: 3px solid var(--ink);
    display: flex;
    align-items: center;
    justify-content: center;
  }
  .song-title {
    margin: 0;
    font-family: "Black Ops One", system-ui, sans-serif;
    font-weight: 400;
    font-size: 38px;
    line-height: 1.55;
    letter-spacing: 2px;
    text-transform: uppercase;
    text-align: center;
    white-space: nowrap;
    color: var(--ink);
  }
  .artist-name {
    position: absolute;
    left: 0;
    right: 0;
    top: 300px;
    margin: 0;
    font-family: "Cinzel", Georgia, serif;
    font-size: 19px;
    letter-spacing: 2px;
    text-transform: uppercase;
    text-align: center;
    color: var(--ink);
  }
  .artist-mark {
    position: absolute;
    right: 18px;
    bottom: 22px;
    width: 122px;
    display: flex;
    flex-direction: column;
    align-items: center;
    gap: 8px;
  }
  .artist-mark-dot {
    width: 34px;
    height: 34px;
    border-radius: 50%;
    background: var(--accent);
  }
  .artist-mark-name {
    font-family: "Cinzel", Georgia, serif;
    font-size: 13px;
    line-height: 1.3;
    text-align: center;
    color: var(--ink);
  }
</style>
</head>
<body>
  <main class="canvas">
    <section class="cover">
      <div class="cover-photo" role="img" aria-label="Photograph of a misty forested mountain slope"></div>
      <div class="title-frame">
        <h1 class="song-title">Marlow and The<br>Lanterns</h1>
      </div>
      <p class="artist-name">Granular Boomkeeperz</p>
      <div class="artist-mark">
        <span class="artist-mark-dot"></span>
        <span class="artist-mark-name">Granular<br>Boomkeeperz</span>
      </div>
    </section>
  </main>
</body>
</html>
```